Business Card for Beach theme sports bar called TORVA

I need a business card designed for our employees, front and back. This will be used by the employees of two business locations to hand out to customers. I've attached the previous business cards we used at one time for a Penwicks (it is now Torva). Looking for a fresh new card that is elegant but has character.

Target Market(s)

30-60, middle class

Contact Information for Business Card

We are a beach bar and sports bar. I am looking for an elegant business card with the front to have the TORVA logo. Then on the back I need it to allow a space for employees to write their names and for them to write in their schedule. I have attached our old cards with our old name Penwicks so you can pull everything we need on the cards. one thing is missing is we have another location at 3158 N Cedar Hollow Rd with a number of 702-418-9035. Since we will use it for both locations it should allow the employee to circle or check mark the bar which they work at.

Font styles to use
Sans Serif

Requirements
Must have
• We are looking for some fresh ideas for the business card. Something that will really stick out to customers when the staff hands them out. Creativity will be looked at positively, but we still want it to look upscale and fun.

```html
<!DOCTYPE html>
<html lang="en">
<head>
<meta charset="utf-8">
<title>Torva Business Card</title>
<link rel="stylesheet" href="https://fonts.googleapis.com/css2?family=Open+Sans:wght@400;600;700&display=swap">
<style>
  :root {
    --backdrop: #6e6e6e;
    --ink: #0b0b0b;
    --paper: #ffffff;
    --rule: #bdbdbd;
    --faint: #1a1a1a;
  }
  html, body {
    margin: 0;
    padding: 0;
    width: 1200px;
    height: 802px;
    overflow: hidden;
    background: var(--backdrop);
    font-family: "Open Sans", Arial, sans-serif;
  }
  .canvas {
    position: relative;
    width: 1200px;
    height: 802px;
  }
  .card {
    position: absolute;
    top: 274px;
    width: 442px;
    height: 265px;
    overflow: hidden;
  }
  .card--schedule { left: 136px; background: var(--paper); }
  .card--brand { left: 624px; background: var(--ink); }

  /* Schedule side */
  .day-strip {
    position: absolute;
    left: 0; top: 0;
    width: 58px; height: 100%;
    background: var(--ink);
  }
  .day-list {
    list-style: none;
    margin: 0; padding: 0;
    position: absolute;
    left: 16px; top: 15px;
  }
  .day {
    width: 28px; height: 25px;
    margin-bottom: 10.5px;
    background: var(--paper);
    border-radius: 4px;
    font-size: 10.5px;
    line-height: 25px;
    text-align: center;
    color: var(--ink);
  }
  .name-rule {
    position: absolute;
    left: 58px; right: 0; top: 130px;
    height: 1px;
    background: var(--rule);
  }
  .locations {
    position: absolute;
    left: 72px; top: 150px;
    font-size: 12.5px;
    line-height: 16px;
    color: #222;
    z-index: 2;
  }
  .location { position: relative; padding-left: 12px; margin-bottom: 8px; }
  .location::before {
    content: "";
    position: absolute;
    left: 0; top: 5px;
    width: 6px; height: 6px;
    border-radius: 50%;
    background: var(--ink);
  }
  .location b { font-weight: 700; }
  .brand-crop {
    position: absolute;
    left: 300px; top: 14px;
    width: 236px; height: 236px;
    border: 2px solid var(--ink);
    border-radius: 50%;
  }
  .brand-name-large {
    position: absolute;
    left: 298px; top: 60px;
    font-size: 78px;
    font-weight: 700;
    color: var(--ink);
    line-height: 1;
    background: var(--paper);
    padding: 0 4px;
  }

  /* Brand side */
  .ghost-ring {
    position: absolute;
    left: -60px; top: 12px;
    width: 240px; height: 240px;
    border: 2px solid var(--faint);
    border-radius: 50%;
  }
  .ghost-name {
    position: absolute;
    left: 0; top: 92px;
    font-size: 72px;
    font-weight: 700;
    color: var(--faint);
    line-height: 1;
  }
  .brand-mark {
    position: absolute;
    left: 167px; top: 79px;
    width: 106px; height: 106px;
    border: 1.5px solid var(--paper);
    border-radius: 50%;
  }
  .brand-name {
    position: absolute;
    left: 0; right: 0; top: 114px;
    text-align: center;
    font-size: 32px;
    font-weight: 700;
    color: var(--paper);
    line-height: 1;
    transform: translateX(0);
  }
</style>
</head>
<body>
<main class="canvas">
  <section class="card card--schedule" aria-label="Schedule side">
    <div class="day-strip">
      <ul class="day-list">
        <li class="day">Mon</li>
        <li class="day">Tue</li>
        <li class="day">Wed</li>
        <li class="day">Thu</li>
        <li class="day">Fri</li>
        <li class="day">Sat</li>
        <li class="day">Sun</li>
      </ul>
    </div>
    <div class="name-rule"></div>
    <div class="brand-crop"></div>
    <div class="brand-name-large">Torva</div>
    <div class="locations">
      <div class="location">3158 N Cedar Hollow Rd<br><b>P:</b> 702-418-9035</div>
      <div class="location">6247 W Marlow Ridge RD<br>Las Vegas, NV 89150<br><b>P:</b> 702-555-0148 | <b>E:</b> cs@torvabar.com</div>
    </div>
  </section>

  <section class="card card--brand" aria-label="Brand side">
    <div class="ghost-ring"></div>
    <div class="ghost-name">Torva</div>
    <div class="brand-mark"></div>
    <div class="brand-name">Torva</div>
  </section>
</main>
</body>
</html>
```